11 x 11 Flyer Design for Social Media - Reverse Mortgages

62 or older?

A Reverse Mortgage
could be
Your Road to Financial Freedom

* No Monthly Payments
* No Income Requirements
* No Credit Score Requirements
* No Loss of Ownership

Receive cash by lump sum, monthly installments or a line of credit!!

Call us today for a Free Consultation!!
(800) 471-2965

Bluegate Financial Services, Inc.
NMLS #318760
www.bluegatehome.com

```html
<!DOCTYPE html>
<html lang="en">
<head>
<meta charset="utf-8">
<title>Reverse Mortgages Flyer</title>
<link href="https://fonts.googleapis.com/css2?family=Oswald:wght@600&family=Poppins:wght@400;500;600;700&display=swap" rel="stylesheet">
<style>
  :root{
    --stage:#2a8fdb;
    --panel:#0a60a9;
    --yellow:#f2f40c;
    --white:#ffffff;
    --ink:#1b1b1b;
    --sand:#ddd6a6;
  }
  html,body{margin:0;padding:0;width:1200px;height:1200px;overflow:hidden;background:var(--stage);}
  .canvas{position:relative;width:1200px;height:1200px;font-family:'Poppins',sans-serif;}
  .flyer{position:absolute;left:108px;top:108px;width:984px;height:984px;background:var(--panel);overflow:hidden;}
  .abs{position:absolute;}
  .brand-box{left:52px;top:0;width:199px;height:189px;background:var(--white);display:flex;align-items:center;justify-content:center;gap:8px;}
  .brand-name{font-weight:600;font-size:19px;line-height:1.25;color:var(--panel);text-align:left;}
  .brand-dot{width:14px;height:14px;border-radius:50%;background:var(--panel);flex:none;}
  .follow{left:708px;top:50px;display:flex;align-items:center;gap:6px;color:var(--white);font-weight:600;font-size:22px;}
  .follow .social{width:29px;height:29px;border-radius:50%;background:var(--white);display:inline-block;}
  .headline{left:46px;top:272px;margin:0;font-family:'Oswald',sans-serif;font-weight:600;font-size:78px;line-height:80px;color:var(--yellow);transform:scaleX(.79);transform-origin:left top;white-space:nowrap;}
  .subhead{left:52px;top:425px;margin:0;font-weight:400;font-size:30px;line-height:39px;color:var(--white);letter-spacing:.5px;white-space:nowrap;}
  .glow-strip{left:290px;top:501px;width:155px;height:32px;background:linear-gradient(90deg,rgba(90,150,200,0),rgba(90,150,200,.55));}
  .benefits-band{left:0;top:533px;width:445px;height:178px;background:linear-gradient(90deg,var(--sand) 0%,#c8cba6 45%,#7fa6b8 78%,#3d7fb7 100%);}
  .benefits{left:50px;top:559px;margin:0;padding:0;list-style:none;font-size:22.8px;line-height:30.5px;color:var(--ink);white-space:nowrap;}
  .payout{left:53px;top:726px;margin:0;font-size:19.5px;line-height:23px;color:var(--white);white-space:nowrap;}
  .cta{left:51px;top:838px;margin:0;font-size:20.5px;color:var(--white);white-space:nowrap;}
  .phone{left:48px;top:866px;margin:0;font-weight:700;font-size:54px;line-height:70px;color:var(--yellow);letter-spacing:1px;white-space:nowrap;}
  .company{left:613px;top:858px;margin:0;font-weight:500;font-size:21px;line-height:25px;color:var(--white);white-space:nowrap;}
  .photo{left:438px;top:230px;width:500px;height:570px;}
</style>
</head>
<body>
<div class="canvas">
  <div class="flyer">
    <div class="abs brand-box">
      <span class="brand-dot"></span>
      <span class="brand-name">Bluegate<br>Financial<br>Services, Inc.</span>
    </div>

    <div class="abs follow">Follow us/ <span class="social"></span><span class="social"></span><span class="social"></span></div>

    <svg class="abs" style="left:812px;top:194px" width="72" height="72" viewBox="0 0 72 72" aria-hidden="true">
      <g fill="#fff">
        <circle cx="5" cy="5" r="4"/><circle cx="26" cy="5" r="4"/><circle cx="47" cy="5" r="4"/><circle cx="68" cy="5" r="4"/>
        <circle cx="5" cy="37" r="3.5"/><circle cx="26" cy="37" r="3.5"/><circle cx="47" cy="37" r="3.5"/><circle cx="68" cy="37" r="3.5"/>
        <circle cx="26" cy="69" r="2"/><circle cx="47" cy="69" r="2"/><circle cx="68" cy="69" r="2"/>
      </g>
    </svg>
    <svg class="abs" style="left:372px;top:372px" width="72" height="72" viewBox="0 0 72 72" aria-hidden="true">
      <g fill="#fff">
        <circle cx="5" cy="5" r="4"/><circle cx="26" cy="5" r="4"/><circle cx="47" cy="5" r="4"/><circle cx="66" cy="5" r="4"/>
        <circle cx="5" cy="37" r="3.5"/><circle cx="26" cy="37" r="3.5"/><circle cx="47" cy="37" r="3.5"/><circle cx="66" cy="37" r="3.5"/>
        <circle cx="5" cy="69" r="2"/><circle cx="26" cy="69" r="2"/><circle cx="47" cy="69" r="2"/><circle cx="66" cy="69" r="2"/>
      </g>
    </svg>

    <h1 class="abs headline">REVERSE<br>MORTGAGES</h1>
    <p class="abs subhead">YOUR ROAD TO<br>FINANCIAL FREEDOM</p>

    <div class="abs glow-strip"></div>
    <div class="abs benefits-band"></div>
    <ul class="abs benefits">
      <li>* No Monthly Payments</li>
      <li>* No Income Requirements</li>
      <li>* No Credit Score Requirements</li>
      <li>* No Loss of Ownership</li>
    </ul>

    <p class="abs payout">Receive cash by lump sum, monthly<br>installments or a line of credit!!</p>

    <svg class="abs photo" viewBox="0 0 500 570">
      <defs>
        <linearGradient id="photoTone" x1="0" y1="0" x2="1" y2="1">
          <stop offset="0" stop-color="#e6d4c0"/>
          <stop offset=".5" stop-color="#d7bfa8"/>
          <stop offset="1" stop-color="#b9a79b"/>
        </linearGradient>
      </defs>
      <path d="M58 8 Q6 10 6 64 L6 510 Q6 564 62 566" fill="none" stroke="#eef4fb" stroke-width="3"/>
      <path role="img" aria-label="Photo of a smiling senior couple reviewing documents with an advisor in their living room" d="M62 14 L440 47 Q497 52 497 110 L497 470 Q497 528 440 533 L62 560 Q14 560 14 510 L14 64 Q14 14 62 14 Z" fill="url(#photoTone)"/>
    </svg>

    <p class="abs cta">Call us today for a Free Consultation!!</p>
    <p class="abs phone">(800) 471-2965</p>

    <p class="abs company">Bluegate Financial Services, Inc.<br>NMLS #318760<br>www.bluegatehome.com</p>
  </div>
</div>
</body>
</html>
```